menu board design: harbor burger

we are a burger restaurant.
we need to re design our menu board to fit within the new design of the restaurant. we are after something simple and easy to read. the overall look and feel of the design should be inline with the design of the shop.

Target Market(s)

18-40 male and female

Colors

Designer to choose colors to be used in the design.

Requirements
Must have
• easy to read. good layout. white background. branding included in design.

```html
<!DOCTYPE html>
<html lang="en">
<head>
<meta charset="utf-8">
<title>Harbor Burger – Menu Board</title>
<link href="https://fonts.googleapis.com/css2?family=Della+Respira&family=Montserrat:wght@400&display=swap" rel="stylesheet">
<style>
  :root {
    --bg: #ffffff;
    --heading-blue: #1ea3e8;
    --item-red: #e3262e;
    --ink: #1d1d1d;
    --brand-blue: #1f56a6;
    --rule: #222222;
  }
  * { margin: 0; padding: 0; box-sizing: border-box; }
  html, body { width: 1200px; height: 600px; overflow: hidden; background: var(--bg); }
  body { font-family: "Della Respira", serif; color: var(--ink); }

  .menu-board { position: relative; width: 1200px; height: 600px; }

  .divider-v { position: absolute; top: 12px; width: 1px; height: 580px; background: var(--rule); }
  .divider-v--one { left: 412px; }
  .divider-v--two { left: 810px; }
  .divider-h { position: absolute; left: 810px; width: 390px; height: 1px; background: var(--rule); }
  .divider-h--one { top: 136px; }
  .divider-h--two { top: 409px; }

  .section-title {
    position: absolute; color: var(--heading-blue); font-size: 34px; line-height: 40px;
    text-align: center; white-space: nowrap; font-weight: 400;
  }
  .section-intro {
    position: absolute; font-size: 16.5px; line-height: 21px; text-align: center; white-space: nowrap;
  }

  .item { position: absolute; }
  .item-head {
    display: flex; justify-content: space-between; align-items: center;
    color: var(--item-red); height: 22px; line-height: 22px;
  }
  .item-name { font-size: 18px; text-transform: uppercase; letter-spacing: -0.2px; white-space: nowrap; }
  .item-price { font-size: 14px; white-space: nowrap; }
  .item-desc { margin-top: 4px; font-size: 13.6px; line-height: 18.5px; }
  .item-desc span { display: block; white-space: nowrap; }

  .col-beef .item { left: 19px; width: 370px; }
  .col-chicken .item { left: 424px; width: 366px; }
  .col-side .item { left: 821px; width: 356px; }

  .nacho-choice { margin-top: 5px; font-size: 15px; line-height: 18px; }
  .nacho-list { margin-top: 7px; font-size: 14.2px; line-height: 18px; }
  .nacho-list span { display: block; white-space: nowrap; }

  .ribs-intro { position: absolute; left: 812px; width: 388px; top: 461px; font-size: 14.2px; line-height: 18.5px; text-align: center; white-space: nowrap; }
  .ribs-packs { position: absolute; left: 821px; width: 363px; top: 504px; font-size: 14.2px; }
  .ribs-pack { display: flex; justify-content: space-between; height: 18.5px; line-height: 18.5px; }
  .ribs-pack .item-price { color: var(--item-red); font-size: 13.5px; }
  .ribs-sauce { position: absolute; left: 821px; top: 563px; font-size: 14.2px; line-height: 20px; white-space: nowrap; }

  .brand { position: absolute; left: 462px; top: 512px; display: flex; align-items: center; gap: 22px; }
  .brand-name { font-family: "Della Respira", serif; color: var(--brand-blue); font-size: 30px; line-height: 1.05; width: 120px; }
  .brand-tagline { font-family: "Montserrat", sans-serif; color: var(--heading-blue); font-size: 10px; letter-spacing: 2.6px; white-space: nowrap; }
</style>
</head>
<body>
<main class="menu-board">
  <div class="divider-v divider-v--one"></div>
  <div class="divider-v divider-v--two"></div>
  <div class="divider-h divider-h--one"></div>
  <div class="divider-h divider-h--two"></div>

  <section class="col-beef">
    <h2 class="section-title" style="left:0;width:412px;top:14px;">Beef Burgers</h2>
    <p class="section-intro" style="left:0;width:412px;top:48px;">All our patties are 100% natural beef.</p>
    <p class="section-intro" style="left:0;width:412px;top:69px;">We know because we grind it ourselves.</p>
    <p class="section-intro" style="left:0;width:412px;top:90px;">Smashed to order on a hot grill rite in front of you.</p>

    <div class="item" style="top:133px;">
      <div class="item-head"><span class="item-name">Classic Beef</span><span class="item-price">8.90</span></div>
      <p class="item-desc"><span>Shredded lettuce, sliced tomato, carmelised onions,</span><span>&nbsp;beetroot and BBQ sauce on a buttered seasame seed bun.</span></p>
    </div>
    <div class="item" style="top:217px;">
      <div class="item-head"><span class="item-name">Cheese Burger</span><span class="item-price">9.50</span></div>
      <p class="item-desc"><span>Dill pickles, minced onion, american cheese, mustard and ketchup</span><span>on a soft milk bun.</span></p>
    </div>
    <div class="item" style="top:302px;">
      <div class="item-head"><span class="item-name">Flame Grill</span><span class="item-price">9.50</span></div>
      <p class="item-desc"><span>Shredded lettuce, sliced tomato, minced onion, dill pickles,</span><span>american cheese, mayo and ketchup on a soft milk bun.</span></p>
    </div>
    <div class="item" style="top:387px;">
      <div class="item-head"><span class="item-name">Big Deck</span><span class="item-price">9.90</span></div>
      <p class="item-desc"><span>Shredded lettuce, dill pickles, minced onion, american cheese</span><span>and special sauce on a soft milk bun.</span></p>
    </div>
    <div class="item" style="top:471px;">
      <div class="item-head"><span class="item-name">Truffled</span><span class="item-price">9.90</span></div>
      <p class="item-desc"><span>Rocket, caramelised onion, dill pickles, havarti cheese and</span><span>truffle infused mayo on a soft milk bun.</span></p>
    </div>
    <div class="item" style="top:556px;">
      <div class="item-head"><span class="item-name">Double Patty</span><span class="item-price">add&nbsp;&nbsp;4.00</span></div>
    </div>
  </section>

  <section class="col-chicken">
    <h2 class="section-title" style="left:412px;width:398px;top:14px;">Chicken Burgers</h2>
    <p class="section-intro" style="left:412px;width:398px;top:48px;">All our chicken burger patties are prepared</p>
    <p class="section-intro" style="left:412px;width:398px;top:69px;">onsite daily using premium quality</p>
    <p class="section-intro" style="left:412px;width:398px;top:90px;">chicken breast.</p>

    <div class="item" style="top:133px;">
      <div class="item-head"><span class="item-name">Classic Chicken</span><span class="item-price">8.90</span></div>
      <p class="item-desc"><span>Shredded lettuce, cheese and mayo on a classic</span><span>seasame seed bun.</span></p>
    </div>
    <div class="item" style="top:217px;">
      <div class="item-head"><span class="item-name">Pirri Pirri</span><span class="item-price">9.50</span></div>
      <p class="item-desc"><span>Shredded lettuce, cheese, mayo and house made pirri pirri</span><span>on a classic seasame seed bun.</span></p>
    </div>
    <div class="item" style="top:302px;">
      <div class="item-head"><span class="item-name">Kentucky</span><span class="item-price">9.90</span></div>
      <p class="item-desc"><span>Shredded lettuce, swiss cheese and feisty mayo on a</span><span>soft milk bun.</span></p>
    </div>
    <div class="item" style="top:387px;">
      <div class="item-head"><span class="item-name">El Burger</span><span class="item-price">9.90</span></div>
      <p class="item-desc"><span>Shredded lettuce, salsa, guacamole, cheese and chipotle</span><span>mayo on a classic sesame seed bun.</span></p>
    </div>
    <div class="item" style="top:462px;">
      <div class="item-head"><span class="item-name">Double Patty</span><span class="item-price">add&nbsp;&nbsp;4.00</span></div>
    </div>

    <div class="brand">
      <span class="brand-name">Harbor Burger</span>
      <span class="brand-tagline">BUILT FRESH EVERY DAY</span>
    </div>
  </section>

  <section class="col-side">
    <h2 class="section-title" style="left:810px;width:390px;top:8px;">Sides</h2>
    <div class="item" style="top:65px;">
      <div class="item-head"><span class="item-name">Fries</span><span class="item-price">3.50</span></div>
    </div>
    <div class="item" style="top:104px;">
      <div class="item-head"><span class="item-name">Kentucky Tenders</span><span class="item-price">6.90</span></div>
    </div>

    <h2 class="section-title" style="left:810px;width:390px;top:146px;">Nachos</h2>
    <div class="item" style="top:203px;">
      <div class="item-head"><span class="item-name">Seasoned Fries</span><span class="item-price">9.90</span></div>
      <p class="nacho-choice">Choose one Guacamole:</p>
      <p class="nacho-list"><span>Salsa Fresca, Guacmole, Jalapenos,</span><span>Cheese Sauce and Sour Cream.</span></p>
    </div>
    <div class="item" style="top:312px;">
      <div class="item-head"><span class="item-name">Freshly Cooked Corn Chips</span><span class="item-price">11.50</span></div>
      <p class="nacho-choice">Choose One Beef Chilli:</p>
      <p class="nacho-list"><span>Salsa Fresca, Beef Chilli, Jalapenos,</span><span>Cheese Sauce and Sour Cream.</span></p>
    </div>

    <h2 class="section-title" style="left:810px;width:395px;top:420px;">Buffalo Chicken Ribs</h2>
    <p class="ribs-intro">Buffalo style fried chicken ribs smothered in one of our<br>mouth-watering sauces, served with a side or Ranch Sauce.</p>
    <div class="ribs-packs">
      <div class="ribs-pack"><span>6 Pack</span><span class="item-price">6.90</span></div>
      <div class="ribs-pack"><span>12 Pack</span><span class="item-price">12.90</span></div>
      <div class="ribs-pack"><span>24 Pack</span><span class="item-price">23.90</span></div>
    </div>
    <p class="ribs-sauce">Choose either Classic Hot Sauce or Smoky BBQ</p>
  </section>
</main>
</body>
</html>
```